Maralby Information Posters for Student signage

Secondary school looking for some posters to display throughout the school with fresh designs using school colours and fitting with general feel of the school's graphic image. The final designs should be welcoming but clearly outline the required instructions. Sample designs that have been created by the school are attached with the relevant information that is required to appear on the signs. School would like a more dynamic design than the basic signs attached.
We are looking for:
- Large pop-up banner style size for the 2 posters called
"Ready for class" and "Morning Routine".
- Printable poster for the "Maralby Outdoor" sign.

Please incorporate a design feature of "the Maralby 1,2,3" into the posters and also use the Maralby Leaner values of Integrity, Compassion, Curiosity and Drive to help illustrate the content.

An option for design is to incorporate our school's first nations artwork into the design and i have also provided various extracts of design pieces that the school often uses in it's marketing materials.

Target Market(s)

Secondary School Students

Industry/Entity Type

Education

Colors
00AB8E
00BBA5
67D7C9
C6EFE9
E9F9F6
FFF300
FFF600
FEFA6F
FFFEC7
FFFEE8
FFC000
F8CF3A
FAE287
FDF2CF
FEFAEE

Requirements
Must have
• My project must have eyecatching graphics

```html
<!DOCTYPE html>
<html lang="en">
<head>
<meta charset="utf-8">
<title>Ready for Class – Maralby</title>
<link href="https://fonts.googleapis.com/css2?family=Archivo+Black&family=Archivo:wght@400;600;700;800&display=swap" rel="stylesheet">
<style>
  :root {
    --green-deep: #1b4420;
    --green-dark: #14361a;
    --green-mid: #2f6b2f;
    --green-leaf: #5fae4a;
    --green-soft: #a9cf9a;
    --yellow: #ffe51a;
    --white: #ffffff;
    --paper: #f7f8f5;
    --ink: #111111;
  }
  * { margin: 0; padding: 0; box-sizing: border-box; }
  html, body { width: 800px; height: 1200px; overflow: hidden; background: var(--white); }
  .poster {
    position: relative; width: 800px; height: 1200px; overflow: hidden;
    background: var(--white);
    font-family: "Archivo", Arial, sans-serif;
    color: var(--green-deep);
  }
  .line-art {
    position: absolute; left: 0; width: 800px;
    background: linear-gradient(180deg, rgba(169,207,154,0) 0%, rgba(169,207,154,.28) 50%, rgba(169,207,154,0) 100%);
  }
  .line-art.upper { top: 50px; height: 130px; }
  .line-art.lower { top: 280px; height: 100px; }
  .emblem-art {
    position: absolute; left: 345px; top: 8px; width: 106px; height: 106px; border-radius: 50%;
    background: radial-gradient(circle, var(--yellow) 0 8%, #fff 10% 18%, #222 30%, #0d0d0d 100%);
  }
  .headline {
    position: absolute; left: 0; width: 800px; text-align: center;
    font-family: "Archivo Black", "Arial Black", sans-serif; line-height: 1;
  }
  .headline.ready { top: 103px; font-size: 140px; letter-spacing: -4px; color: var(--green-deep); }
  .headline.for-class {
    top: 222px; font-size: 82px; color: var(--yellow); letter-spacing: -1px;
    -webkit-text-stroke: 4px var(--green-deep); paint-order: stroke fill;
  }
  .tagline {
    position: absolute; top: 296px; left: 0; width: 800px; text-align: center;
    font-weight: 600; font-size: 19px; line-height: 1.15; color: var(--ink);
  }
  .ground-art {
    position: absolute; left: 0; top: 400px; width: 800px; height: 800px;
    background:
      radial-gradient(circle at 70px 240px, rgba(95,174,74,.55) 0 90px, transparent 170px),
      radial-gradient(circle at 730px 210px, rgba(95,174,74,.7) 0 80px, transparent 130px),
      radial-gradient(circle at 740px 470px, rgba(169,207,154,.35) 0 70px, transparent 110px),
      linear-gradient(180deg, var(--green-mid) 0%, var(--green-deep) 45%, #0c2410 100%);
    border-top: 6px solid var(--yellow);
    border-radius: 40% 40% 0 0 / 30px 30px 0 0;
  }
  .steps-card {
    position: absolute; left: 150px; top: 416px; width: 500px; height: 604px;
    background: var(--paper); border: 7px solid var(--yellow); border-radius: 30px;
  }
  .steps-tab {
    position: absolute; left: 186px; top: 350px; width: 444px; height: 147px;
    background: var(--white); border: 6px solid var(--green-deep); border-radius: 26px; overflow: hidden;
    outline: 2px dashed var(--green-deep); outline-offset: -12px;
  }
  .steps-tab .tab-title {
    height: 70px; display: flex; align-items: center; justify-content: center;
    font-family: "Archivo Black", "Arial Black", sans-serif; font-size: 46px; color: var(--green-deep);
  }
  .steps-tab .tab-numbers {
    height: 65px; background: var(--yellow);
    display: flex; align-items: center; justify-content: center; gap: 18px;
  }
  .tab-numbers .dots { font-weight: 800; font-size: 22px; letter-spacing: 6px; color: var(--green-deep); }
  .num-badge {
    width: 42px; height: 42px; border-radius: 50%; background: var(--green-deep); color: var(--white);
    display: flex; align-items: center; justify-content: center;
    font-family: "Archivo Black", "Arial Black", sans-serif; font-size: 27px;
  }
  .step { position: absolute; left: 202px; width: 440px; height: 146px; display: flex; align-items: center; }
  .step.one { top: 511px; }
  .step.two { top: 667px; }
  .step.three { top: 830px; }
  .step-icon {
    width: 146px; height: 146px; border-radius: 50%; flex: none;
    border: 3px dashed var(--yellow); padding: 8px;
  }
  .step-icon .art { width: 100%; height: 100%; border-radius: 50%; }
  .step.one .art { background: radial-gradient(circle at 50% 45%, #3b3b3b 0 28%, var(--green-deep) 30%); }
  .step.two .art { background: radial-gradient(ellipse 22% 40% at 50% 50%, var(--green-deep) 0 98%, var(--yellow) 100%); }
  .step.three .art { background: radial-gradient(ellipse 40% 22% at 50% 55%, var(--green-deep) 0 98%, var(--green-leaf) 100%); }
  .step-badge {
    margin-left: 20px; width: 56px; height: 56px; border-radius: 50%; flex: none;
    border: 4px solid var(--green-deep); background: var(--yellow);
    display: flex; align-items: center; justify-content: center;
  }
  .step-badge span {
    width: 42px; height: 42px; border-radius: 50%; background: var(--green-deep); color: var(--white);
    display: flex; align-items: center; justify-content: center;
    font-family: "Archivo Black", "Arial Black", sans-serif; font-size: 27px;
  }
  .step-label { margin-left: 12px; font-weight: 800; font-size: 34px; line-height: 1.1; color: var(--green-deep); }
  .step-label small { display: block; font-weight: 600; font-size: 23px; color: var(--ink); margin-top: 2px; }
  .values { position: absolute; left: 161px; top: 1028px; color: var(--white); }
  .values .value-pair { font-weight: 800; font-size: 46px; letter-spacing: -.5px; line-height: 1.1; }
  .values .value-caption { font-weight: 400; font-size: 28px; color: var(--yellow); margin-top: 4px; padding-left: 63px; }
  .school-mark { position: absolute; left: 598px; top: 1040px; display: flex; align-items: center; gap: 10px; }
  .school-mark .mark-dot { width: 24px; height: 24px; border-radius: 50%; background: var(--yellow); }
  .school-mark .mark-name { font-weight: 800; font-size: 30px; color: var(--white); }
</style>
</head>
<body>
<main class="poster">
  <div class="line-art upper" role="img" aria-label="Faint green dotted First Nations flowing line artwork"></div>
  <div class="line-art lower" role="img" aria-label="Faint green dotted First Nations flowing line artwork"></div>
  <div class="emblem-art" role="img" aria-label="Round First Nations dot artwork in black, white and yellow"></div>

  <h1 class="headline ready">READY</h1>
  <p class="headline for-class">FOR CLASS?</p>
  <p class="tagline">You’ve got what it takes.<br>Let’s make today a great one!</p>

  <div class="ground-art" role="img" aria-label="Green First Nations dot painting artwork with circular motifs and a globe"></div>

  <section class="steps-card" aria-label="The Maralby 1, 2, 3"></section>
  <div class="steps-tab">
    <div class="tab-title">The Maralby</div>
    <div class="tab-numbers">
      <span class="num-badge">1</span><span class="dots">···</span>
      <span class="num-badge">2</span><span class="dots">···</span>
      <span class="num-badge">3</span>
    </div>
  </div>

  <div class="step one">
    <div class="step-icon"><div class="art" role="img" aria-label="Laptop with school crest on screen"></div></div>
    <div class="step-badge"><span>1</span></div>
    <div class="step-label">Laptop /<br>Workbook</div>
  </div>
  <div class="step two">
    <div class="step-icon"><div class="art" role="img" aria-label="Green Pouchly phone pouch"></div></div>
    <div class="step-badge"><span>2</span></div>
    <div class="step-label">Phone in<br>Pouchly</div>
  </div>
  <div class="step three">
    <div class="step-icon"><div class="art" role="img" aria-label="Green school bucket hat with yellow band"></div></div>
    <div class="step-badge"><span>3</span></div>
    <div class="step-label">Correct<br>Uniform<small>(including hat)</small></div>
  </div>

  <div class="values">
    <div class="value-pair">Curiosity &amp; Drive</div>
    <div class="value-caption">Maralby Learner Values</div>
  </div>

  <div class="school-mark">
    <span class="mark-dot"></span>
    <span class="mark-name">Maralby</span>
  </div>
</main>
</body>
</html>
```